Bref créative
The Marlowe Gala
Event Planning
Professional
Rosalind Hartwell
Owner - The Marlowe Gala
4105 - 27 Ashcombe Avenue
Toronto, ON M5R 2K7
rosalind@TheMarloweGala.example
www.TheMarloweGala.example
The card can be single or double sided i don't mind. Just be creative and make it clean!!!
Thanks!
It can be single or double sided I dont mind.

```html
<!DOCTYPE html>
<html lang="en">
<head>
<meta charset="utf-8">
<title>The Marlowe Gala — Business Cards</title>
<link rel="stylesheet" href="https://fonts.googleapis.com/css2?family=Questrial&display=swap">
<style>
  :root {
    --backdrop: #d9d5d0;
    --paper: #f4f4f4;
    --paper-shade: #dcdcdc;
    --slate: #6b6b6b;
    --slate-dark: #555555;
    --silver-light: #e6e6e6;
    --silver-dark: #9a9a9a;
    --ink: #5a5a5a;
    --ink-soft: #777777;
    --white: #ffffff;
  }
  * { margin: 0; padding: 0; box-sizing: border-box; }
  html, body { width: 1200px; height: 995px; overflow: hidden; }
  body {
    background: var(--backdrop);
    font-family: "Questrial", "Century Gothic", sans-serif;
    position: relative;
  }
  .card {
    position: absolute;
    border-radius: 24px;
    overflow: hidden;
    box-shadow: 0 14px 28px rgba(0,0,0,0.28);
  }

  /* Contact side */
  .card--contact {
    left: 270px; top: 162px; width: 595px; height: 283px;
    background: var(--slate);
  }
  .card--contact .panel-light {
    position: absolute; left: 0; top: 0; bottom: 0; width: 260px;
    background: linear-gradient(160deg, var(--white) 0%, var(--paper) 55%, var(--paper-shade) 100%);
    border-top-right-radius: 40px 140px;
    border-bottom-right-radius: 40px 140px;
  }
  .card--contact .name-band {
    position: absolute; left: 260px; right: 0; top: 22px; height: 50px;
    background: linear-gradient(90deg, var(--silver-light), var(--silver-dark));
    padding: 7px 0 0 26px;
    color: var(--ink);
    font-size: 14px; line-height: 18px;
  }
  .card--contact .details {
    position: absolute; left: 286px; top: 112px;
    color: var(--white); font-size: 13px; line-height: 17px;
  }
  .card--contact .details .address { margin-bottom: 26px; }
  .card--contact .details li { list-style: none; }
  .card--contact .details li::before { content: "\2022"; margin-right: 6px; }

  .brand {
    position: absolute; left: 0; right: 0;
    text-align: center;
  }
  .brand__mark {
    display: block; margin: 0 auto 14px;
    width: 64px; height: 64px;
  }
  .brand__name {
    display: block; font-size: 19px; letter-spacing: 1.5px; text-transform: uppercase;
  }
  .brand__tagline {
    display: block; font-size: 12px; letter-spacing: 3px; margin-top: 3px;
  }
  .card--contact .brand { width: 260px; top: 82px; color: var(--ink); }
  .card--contact .brand__mark { background: var(--slate); }

  /* White front */
  .card--front-light {
    left: 175px; top: 500px; width: 440px; height: 310px;
    background: linear-gradient(170deg, var(--white) 0%, var(--paper) 60%, var(--paper-shade) 100%);
  }
  .card--front-light .brand { top: 80px; color: var(--ink); }
  .card--front-light .brand__mark { background: var(--slate); }
  .web-strip {
    position: absolute; left: 0; right: 0; height: 22px;
    font-size: 12px; letter-spacing: 3px; line-height: 22px;
    padding-left: 90px;
  }
  .card--front-light .web-strip {
    bottom: 38px; background: var(--slate); color: var(--white);
  }

  /* Grey front */
  .card--front-dark {
    left: 540px; top: 560px; width: 485px; height: 305px;
    background: linear-gradient(170deg, var(--slate) 0%, var(--slate-dark) 100%);
  }
  .card--front-dark .brand { top: 72px; color: var(--white); }
  .card--front-dark .brand__mark { background: var(--white); }
  .card--front-dark .web-strip {
    bottom: 40px; padding-left: 110px;
    background: linear-gradient(90deg, var(--silver-dark), var(--silver-light) 70%, var(--silver-dark));
    color: var(--ink);
  }
</style>
</head>
<body>

  <section class="card card--contact" aria-label="Contact side">
    <div class="panel-light"></div>
    <div class="brand">
      <span class="brand__mark"></span>
      <span class="brand__name">The Marlowe Gala</span>
      <span class="brand__tagline">Event Planning</span>
    </div>
    <div class="name-band">
      <p class="person">Rosalind Hartwell</p>
      <p class="role">Owner - The Marlowe Gala</p>
    </div>
    <div class="details">
      <p class="address">4105 - 27 Ashcombe Avenue<br>Toronto, ON M5R 2K7</p>
      <ul>
        <li>t 416.555.0142</li>
        <li>c 416.555.0187</li>
        <li>f 416.555.0163</li>
        <li>rosalind@TheMarloweGala.example</li>
        <li>www.TheMarloweGala.example</li>
      </ul>
    </div>
  </section>

  <section class="card card--front-light" aria-label="Light front">
    <div class="brand">
      <span class="brand__mark"></span>
      <span class="brand__name">The Marlowe Gala</span>
      <span class="brand__tagline">Event Planning</span>
    </div>
    <p class="web-strip">www.TheMarloweGala.example</p>
  </section>

  <section class="card card--front-dark" aria-label="Dark front">
    <div class="brand">
      <span class="brand__mark"></span>
      <span class="brand__name">The Marlowe Gala</span>
      <span class="brand__tagline">Event Planning</span>
    </div>
    <p class="web-strip">www.TheMarloweGala.example</p>
  </section>

</body>
</html>
```